Simple and Approachable Cover for Pet Expo Company Page

Size: 2000 x 430; looking simply for words "Tenbury HR Consulting" and email address "TenburyHRConsulting@mailvane.com." This is for a cover photo for a company profile page for the Northway Animal Fair, where I am a featured speaker on Employee Communications later this month. You can incorporate the attached photo to the left of the banner ad if you wish. The mood I wish to present is approachable, positive and simple.

Target Market(s)

small pet retail business owners

Industry/Entity Type

Pet Shop

Font styles to use
Serif
Sans Serif

Requirements
Must have
• Email address clearly defined/separated. Easy to read.
Nice to have
• I like the picture that I included; subtle pet paw background is also nice
Should not have
• No paid stock images

```html
<!DOCTYPE html>
<html lang="en">
<head>
<meta charset="UTF-8">
<title>Tenbury HR Consulting – Cover Banners</title>
<link href="https://fonts.googleapis.com/css2?family=Fredoka:wght@700&family=Poppins:wght@500&display=swap" rel="stylesheet">
<style>
  :root {
    --page: #ffffff;
    --sun: #fcd000;
    --sun-deep: #f2b300;
    --teal: #00adb5;
    --teal-bright: #00c8d2;
    --navy: #1b2a3d;
    --white: #ffffff;
    --photo-sky: #9fb87a;
    --photo-grass: #6f8a4a;
    --photo-warm: #c79a6b;
  }
  * { margin: 0; padding: 0; box-sizing: border-box; }
  html, body {
    width: 1200px; height: 900px; overflow: hidden;
    background: var(--page);
  }
  .sheet { position: relative; width: 1200px; height: 900px; }

  .banner {
    position: absolute; left: 63px; width: 1074px; height: 231px;
    overflow: hidden;
    box-shadow: 0 3px 6px rgba(0,0,0,0.28);
  }
  .banner--sun { top: 194px; --base: var(--sun); --base-deep: var(--sun-deep); --accent: var(--teal); }
  .banner--teal { top: 466px; --base: var(--teal-bright); --base-deep: var(--teal); --accent: var(--sun); }

  .banner__art { position: absolute; inset: 0; width: 100%; height: 100%; }
  .bg-fill { fill: var(--base); }
  .bg-glow { fill: var(--base-deep); opacity: 0.35; }
  .photo-rim { fill: var(--accent); }
  .photo-frame { stroke: var(--white); stroke-width: 5; }

  .banner__title {
    position: absolute; left: 30px; top: 63px;
    font-family: "Fredoka", sans-serif; font-weight: 700;
    font-size: 46px; line-height: 1; letter-spacing: -0.3px;
    color: var(--navy);
    -webkit-text-stroke: 6px var(--white);
    paint-order: stroke fill;
    text-shadow: 0 3px 6px rgba(0,0,0,0.22);
    white-space: nowrap;
  }
  .banner__email-band {
    position: absolute; left: 0; top: 125px;
    width: 628px; height: 48px;
    background: var(--accent);
    border-radius: 0 24px 24px 0;
  }
  .banner__email {
    position: absolute; left: 30px; top: 50%;
    transform: translateY(-52%);
    font-family: "Poppins", sans-serif; font-weight: 500;
    font-size: 26px; letter-spacing: 2.1px;
    color: var(--white);
    white-space: nowrap;
  }
</style>
</head>
<body>
<main class="sheet">

  <section class="banner banner--sun">
    <svg class="banner__art" viewBox="0 0 1074 231" preserveAspectRatio="none">
      <defs>
        <linearGradient id="photoToneA" x1="0" y1="0" x2="0" y2="1">
          <stop offset="0" stop-color="var(--photo-sky)"/>
          <stop offset="0.55" stop-color="var(--photo-warm)"/>
          <stop offset="1" stop-color="var(--photo-grass)"/>
        </linearGradient>
      </defs>
      <rect class="bg-fill" width="1074" height="231"/>
      <circle class="bg-glow" cx="565" cy="190" r="150"/>
      <circle class="bg-glow" cx="700" cy="231" r="120"/>
      <path class="photo-rim" d="M790 231 C770 170 790 105 840 85 C860 35 910 0 980 0 L1074 0 L1074 231 Z"/>
      <path class="photo-frame" role="img" aria-label="Photo of the two consultants sitting on grass outdoors with their two hound dogs"
            fill="url(#photoToneA)"
            d="M805 231 C785 170 805 115 845 100 C860 45 910 8 985 8 C1010 8 1030 25 1074 40 L1074 170 C1040 178 1010 195 990 231 Z"/>
    </svg>
    <h1 class="banner__title">TENBURY HR CONSULTING</h1>
    <div class="banner__email-band">
      <p class="banner__email">TenburyHRConsulting@mailvane.com</p>
    </div>
  </section>

  <section class="banner banner--teal">
    <svg class="banner__art" viewBox="0 0 1074 231" preserveAspectRatio="none">
      <defs>
        <linearGradient id="photoToneB" x1="0" y1="0" x2="0" y2="1">
          <stop offset="0" stop-color="var(--photo-sky)"/>
          <stop offset="0.55" stop-color="var(--photo-warm)"/>
          <stop offset="1" stop-color="var(--photo-grass)"/>
        </linearGradient>
      </defs>
      <rect class="bg-fill" width="1074" height="231"/>
      <circle class="bg-glow" cx="565" cy="190" r="150"/>
      <circle class="bg-glow" cx="700" cy="231" r="120"/>
      <path class="photo-rim" d="M790 231 C770 170 790 105 840 85 C860 35 910 0 980 0 L1074 0 L1074 231 Z"/>
      <path class="photo-frame" role="img" aria-label="Photo of the two consultants sitting on grass outdoors with their two hound dogs"
            fill="url(#photoToneB)"
            d="M805 231 C785 170 805 115 845 100 C860 45 910 8 985 8 C1010 8 1030 25 1074 40 L1074 170 C1040 178 1010 195 990 231 Z"/>
    </svg>
    <h2 class="banner__title">TENBURY HR CONSULTING</h2>
    <div class="banner__email-band">
      <p class="banner__email">TenburyHRConsulting@mailvane.com</p>
    </div>
  </section>

</main>
</body>
</html>
```